Hunting Ethics Organization Needs a Web Design with Logo Refresh

This project involves the creation of a website design including the homepage design, inside page design, and logo refinements. Our organization is Talvera, and we are a not-for-profit hunting ethics organization.
The focus of the new website design is to bring attention the mission of our organization, provide an overview of the areas where our organization deploys its resources to support the modern hunter, and to encourage visitors to support our organization by donating in support of the organization’s mission.
The winning design will be implemented in Wordpress by our in-house team. If you have questions about how any particular design element may translate to Wordpress, please feel free to post questions in response to this brief. In general, however, we’re more focused on the evolution and delivery of a strong overall design aesthetic – we’ll shoulder the responsibility of how we translate that design into Wordpress.
See attached design brief for full details.

```html
<!DOCTYPE html>
<html lang="en">
<head>
<meta charset="utf-8">
<title>Talvera – The Hunter's Institute</title>
<link href="https://fonts.googleapis.com/css2?family=Nunito:wght@400;600;700&family=Nunito+Sans:wght@400;600&display=swap" rel="stylesheet">
<style>
:root{
  --navy:#0b2f84;
  --olive:#a39b58;
  --olive-light:#c8c27a;
  --ink:#2b2b2b;
  --grey:#555;
  --footer:#3c3c3c;
  --white:#fff;
}
*{box-sizing:border-box;margin:0;padding:0}
html,body{width:1075px;height:1200px;overflow:hidden;background:var(--white)}
body{position:relative;font-family:"Nunito Sans",sans-serif;color:var(--ink)}
.abs{position:absolute}

/* header */
.site-header{position:absolute;left:0;top:0;width:1075px;height:83px}
.brand{position:absolute;left:68px;top:30px;display:flex;align-items:center;gap:6px}
.brand-dot{width:20px;height:20px;border-radius:50%;background:var(--olive)}
.brand-text{display:flex;flex-direction:column;line-height:1}
.brand-name{font-family:"Nunito",sans-serif;font-weight:700;font-size:25px;color:var(--navy);letter-spacing:.5px}
.brand-tag{font-size:8.5px;color:var(--navy);margin-top:2px}
.nav-link{position:absolute;top:45px;font-size:11px;color:var(--ink);white-space:nowrap}
.donate-btn{position:absolute;left:928px;top:34px;width:80px;height:36px;background:var(--olive);color:var(--white);font-size:11.5px;display:flex;align-items:center;justify-content:center}

/* hero */
.hero{position:absolute;left:0;top:83px;width:1075px;height:369px;
  background:linear-gradient(90deg,#6b5e3c 0%,#7a6a42 40%,#85703f 62%,#6e6340 80%,#5e5a3e 100%)}
.hero-copy{position:absolute;left:68px;top:87px;color:var(--white)}
.hero-title{font-family:"Nunito",sans-serif;font-weight:700;font-size:21px;line-height:27px;width:480px}
.hero-list{list-style:none;margin-top:6px;font-size:21px;line-height:29px;font-weight:400}
.hero-list li::before{content:"»";font-size:15px;margin-right:10px}
.hero-dots{position:absolute;left:67px;top:410px;display:flex;gap:7px}
.hero-dots i{width:12px;height:12px;border-radius:50%;background:var(--white)}
.hero-dots i:first-child{background:var(--olive-light)}

/* cards */
.card{position:absolute;top:477px;width:296px;height:175px}
.card-img{height:128px}
.card-label{height:47px;background:var(--navy);color:var(--white);font-family:"Nunito",sans-serif;font-size:19.5px;padding:11px 16px}
.divider{position:absolute;left:0;top:695px;width:1075px;height:8px;
  background:radial-gradient(ellipse at top,rgba(0,0,0,.12),rgba(0,0,0,0) 70%)}

/* about */
.about-title{left:67px;top:734px;font-family:"Nunito",sans-serif;font-size:26px;font-weight:600;color:var(--navy)}
.about-sub{left:67px;top:763px;font-family:"Nunito",sans-serif;font-size:22px;color:var(--grey)}
.about-text{left:67px;top:801px;width:625px;font-size:10.4px;line-height:19px;color:#333}
.about-text p+p{margin-top:6px}
.read-btn{left:67px;top:961px;width:104px;height:36px;background:var(--olive);color:var(--white);font-size:11px;display:flex;align-items:center;justify-content:center}
.watch-title{left:711px;top:745px;font-family:"Nunito",sans-serif;font-size:25px;color:var(--grey)}
.watch-title b{color:var(--navy);font-weight:600}
.video{left:711px;top:809px;width:298px;height:188px;background:linear-gradient(180deg,#6a5a48,#4f5346 55%,#3a4350)}
.video svg{position:absolute;left:122px;top:67px}

/* footer */
.site-footer{position:absolute;left:0;top:1025px;width:1075px;height:175px;background:var(--footer);color:var(--white)}
.f-brand{left:68px;top:36px;display:flex;align-items:center;gap:6px}
.f-brand .brand-name,.f-brand .brand-tag{color:var(--white)}
.f-brand .brand-name{font-size:27px}
.copy{left:69px;top:99px;font-size:11px;line-height:19px}
.f-head{font-size:13.5px;font-weight:600}
.f-col{top:32px}
.f-text{font-size:11px;line-height:17px;margin-top:8px}
.email-field{position:absolute;left:0;top:90px;width:219px;height:34px;background:var(--white);color:#999;font-style:italic;font-size:10.5px;padding:10px 12px}
.signup{position:absolute;left:230px;top:90px;width:69px;height:34px;background:var(--olive);font-size:11px;display:flex;align-items:center;justify-content:center}
.socials{display:flex;gap:7px;margin-top:13px}
.socials i{width:26px;height:26px;border-radius:50%;background:#2f5fa8}
.socials i:last-child{background:#c92a2a}
.contact a{color:var(--olive-light);text-decoration:none}
</style>
</head>
<body>

<header class="site-header">
  <div class="brand">
    <div class="brand-dot"></div>
    <div class="brand-text"><span class="brand-name">TALVERA</span><span class="brand-tag">THE HUNTER'S INSTITUTE</span></div>
  </div>
  <nav>
    <span class="nav-link" style="left:326px">HOME</span>
    <span class="nav-link" style="left:393px">ABOUT US</span>
    <span class="nav-link" style="left:482px">HUNTING ETHICS</span>
    <span class="nav-link" style="left:609px">CONSERVATION</span>
    <span class="nav-link" style="left:727px">GET INVOLVED</span>
    <span class="nav-link" style="left:840px">CONTACT US</span>
  </nav>
  <div class="donate-btn">DONATE</div>
</header>

<section class="hero" role="img" aria-label="Hunter in orange cap and vest carrying a shotgun through tall autumn grass with a dog">
  <div class="hero-copy">
    <h1 class="hero-title">Make an emotional appeal that connects the visitor and encourages them to get involved or make a donation:</h1>
    <ul class="hero-list">
      <li>“Protect the heritage of hunting”</li>
      <li>“Help us protect the future of hunting”</li>
      <li>“Support us as we empower the modern hunter”</li>
    </ul>
  </div>
</section>
<div class="hero-dots"><i></i><i></i><i></i><i></i></div>

<article class="card" style="left:67px">
  <div class="card-img" role="img" aria-label="Hunter in camouflage aiming a rifle in the forest" style="background:linear-gradient(180deg,#72805c,#8a7a62)"></div>
  <div class="card-label">Hunting Ethics</div>
</article>
<article class="card" style="left:389px">
  <div class="card-img" role="img" aria-label="Two hunters in camouflage walking through a field" style="background:linear-gradient(180deg,#a3a3a2,#7a725f)"></div>
  <div class="card-label">Conservation</div>
</article>
<article class="card" style="left:711px">
  <div class="card-img" role="img" aria-label="Young woman hunter in camouflage among foliage" style="background:linear-gradient(180deg,#5d6a58,#6e6458)"></div>
  <div class="card-label">Get Involved</div>
</article>

<div class="divider"></div>

<h2 class="abs about-title">TALVERA</h2>
<div class="abs about-sub">The Hunter Institute</div>
<div class="abs about-text">
  <p>Aliquam molestie, mi et imperdiet euismod, dui purus auctor tellus, et interdum lacus lectus et ante. Sed accumsan sollicitudin sapien, sit amet adipiscing turpis gravida ac. In congue, neque ac lobortis volutpat, libero mauris varius mi, vitae suscipit ipsum ligula vitae risus. Duis aliquam nibh a dui iaculis viverra id a velit. Vivamus egestas risus in magna varius commodo. Sed semper viverra egestas. Etiam pretium porttitor lectus, vel ornare neque porta volutpat.</p>
  <p>Aenean a nibh eget turpis vehicula tempus ac sed massa. Vestibulum dolor nulla, ultrices ac tincidunt sed, laoreet non est. Suspendisse lobortis turpis in odio blandit ac interdum lorem euismod. Etiam risus massa, vulputate eu pellentesque et, consectetur a neque.</p>
</div>
<div class="abs read-btn">READ MORE</div>

<h2 class="abs watch-title"><b>WATCH</b> The Video</h2>
<div class="abs video" role="img" aria-label="Two anglers wading in a river with a landing net">
  <svg width="54" height="54" viewBox="0 0 54 54"><circle cx="27" cy="27" r="25" fill="none" stroke="#fff" stroke-width="3"/><path d="M21 15 L39 27 L21 39 Z" fill="#fff"/></svg>
</div>

<footer class="site-footer">
  <div class="abs f-brand">
    <div class="brand-dot" style="background:#fff"></div>
    <div class="brand-text"><span class="brand-name">TALVERA</span><span class="brand-tag">THE HUNTER'S INSTITUTE</span></div>
  </div>
  <div class="abs copy">Copyright ©2015.Talvera.<br>All Right Reserved</div>

  <div class="abs f-col" style="left:307px;width:310px;height:140px">
    <div class="f-head">STAY INFORMED</div>
    <div class="f-text">Sign up for breaking news on wildlife and<br>conservation issues:</div>
    <div class="email-field">Enter Email Address</div>
    <div class="signup">SIGN UP</div>
  </div>

  <div class="abs f-col" style="left:648px">
    <div class="f-head">CONNECT WITH US</div>
    <div class="socials"><i></i><i></i><i></i><i></i></div>
  </div>

  <div class="abs f-col contact" style="left:843px">
    <div class="f-head">CONTACT US</div>
    <div class="f-text">TALVERA<br><span style="display:block;margin-top:4px">412 Heather Lane<br>Road,Dunmore, K17 4TR</span>
      <span style="display:block;margin-top:4px">Ph: <a>555-014-2236</a></span>
      <span style="display:block;margin-top:4px">Email: <a>info@talvera.org</a></span></div>
  </div>
</footer>

</body>
</html>
```